Deaths in the gang

Creation of a cover for the book "Un soir de pluie" (Title to be used, not the English one)
Size: 14 x 20.5 cm (vertical; with bleed-off on the top, the right side and the bottom)
Title: “One rainy evening” (this title has no meaning, it's just an expression)
Author: "Mathieu Dervanche"
Publisher: “Editions Pavane” (at the bottom of the page).
Key Words:
gangster, escape, hold up, murders, jewels, love, young woman with auburn hair.
Story:
Julien Marbot, a very dangerous gangster and unscrupulous murderer, escapes from prison in order to organize a new hold up. Lieutenant Vidal, one of the police officers in charge of the investigation falls in love with Sandrine Moulet, a lovely prison supervisor who has been held hostage during the escape of Marbot.
But Vidal realizes that Sandrine doesn't tell him all the truth.
And soon, several members of the gang die in mysterious circumstances…
The unbelievable truth will be revealed tardily.
Target Market(s)
Readers of detective stories
Industry/Entity Type
Book
Look and feel

```html
<!DOCTYPE html>
<html lang="fr">
<head>
<meta charset="utf-8">
<title>Un soir de pluie — Mathieu Dervanche</title>
<link rel="stylesheet" href="https://fonts.googleapis.com/css2?family=Cinzel:wght@400;600;700&display=swap">
<style>
  :root {
    --page-bg: #ffffff;
    --cover-black: #050505;
    --title-white: #f3f3f3;
    --title-red: #c8333f;
    --hair-red: #c42a3a;
    --hair-deep: #8e1c2e;
    --hair-dark: #5a1424;
    --skin: #ead3c6;
    --skin-shade: #c9a49a;
    --mist-pink: #d9a3bb;
    --mist-white: #f4eef0;
    --shadow-green: #2f4a44;
    --text-shadow: rgba(60, 8, 20, 0.75);
  }
  html, body {
    margin: 0;
    padding: 0;
    width: 1200px;
    height: 1200px;
    overflow: hidden;
    background: var(--page-bg);
  }
  .book-cover {
    position: absolute;
    left: 233px;
    top: 50px;
    width: 733px;
    height: 1100px;
    background: var(--cover-black);
    overflow: hidden;
  }
  .cover-illustration {
    position: absolute;
    left: 0;
    top: 0;
    width: 733px;
    height: 880px;
    background:
      radial-gradient(ellipse 22% 26% at 66% 46%, var(--skin) 0%, rgba(234,211,198,0.7) 55%, rgba(234,211,198,0) 100%),
      radial-gradient(ellipse 30% 22% at 62% 66%, var(--skin-shade) 0%, rgba(201,164,154,0) 100%),
      radial-gradient(ellipse 60% 18% at 52% 9%, var(--hair-red) 0%, rgba(196,42,58,0.85) 55%, rgba(196,42,58,0) 100%),
      radial-gradient(ellipse 32% 34% at 24% 32%, var(--hair-red) 0%, rgba(196,42,58,0.6) 55%, rgba(196,42,58,0) 100%),
      radial-gradient(ellipse 18% 40% at 94% 32%, var(--mist-pink) 0%, rgba(217,163,187,0) 100%),
      radial-gradient(ellipse 20% 34% at 14% 62%, var(--hair-dark) 0%, rgba(90,20,36,0) 100%),
      radial-gradient(ellipse 14% 40% at 88% 58%, var(--hair-deep) 0%, rgba(142,28,46,0) 100%),
      radial-gradient(ellipse 18% 20% at 97% 80%, var(--shadow-green) 0%, rgba(47,74,68,0) 100%),
      radial-gradient(ellipse 18% 20% at 8% 82%, var(--shadow-green) 0%, rgba(47,74,68,0) 100%),
      linear-gradient(90deg, var(--mist-white) 0%, rgba(244,238,240,0) 8%),
      linear-gradient(180deg, #e7cdd6 0%, #e3c2cc 40%, #7e5a5c 64%, #2a1a1c 80%, var(--cover-black) 100%);
  }
  .cover-illustration::after {
    content: "";
    position: absolute;
    inset: 0;
    background: linear-gradient(180deg, rgba(5,5,5,0) 58%, rgba(5,5,5,0.85) 86%, var(--cover-black) 100%);
  }
  .cover-type {
    position: absolute;
    left: 0;
    top: 0;
    width: 733px;
    height: 1100px;
  }
  .author-name {
    font-family: "Cinzel", serif;
    font-weight: 400;
    font-size: 48px;
    fill: var(--title-white);
    filter: drop-shadow(0 1px 3px var(--text-shadow));
  }
  .title-line-one {
    font-family: "Cinzel", serif;
    font-weight: 700;
    font-size: 118px;
    fill: var(--title-white);
  }
  .title-line-two {
    font-family: "Cinzel", serif;
    font-weight: 700;
    font-size: 152px;
    fill: var(--title-red);
  }
  .publisher-name {
    font-family: "Cinzel", serif;
    font-weight: 400;
    font-size: 32px;
    fill: var(--title-white);
  }
</style>
</head>
<body>
  <main class="book-cover">
    <div class="cover-illustration" role="img" aria-label="Painted portrait of a young woman with auburn hair, a smear of blood on her cheek, on a pink and white watercolour background fading into black"></div>
    <svg class="cover-type" viewBox="0 0 733 1100" xmlns="http://www.w3.org/2000/svg">
      <text class="author-name" x="96" y="92" textLength="548" lengthAdjust="spacingAndGlyphs">MATHIEU DERVANCHE</text>
      <text class="title-line-one" x="62" y="817" textLength="635" lengthAdjust="spacingAndGlyphs">UN SOIR</text>
      <text class="title-line-two" x="62" y="938" textLength="635" lengthAdjust="spacingAndGlyphs">DE PLUIE</text>
      <text class="publisher-name" x="269" y="1069" textLength="288" lengthAdjust="spacingAndGlyphs">Editions Pavane</text>
    </svg>
  </main>
</body>
</html>
```